Visual for a Mobile Repair Shop Window

We need a advertising for shop window.
We repair all mobiles phone and tablet, 100 hundred shop all around France and start to repair laptops with Atelier Grenat (green logo) partnership (but don't just put AG logo in red/grey design...).

Customer must quickly understand that we can repair or help him with his mobile problem.

Dimension : 200 cm x 200 cm
Need PSD file for adaptation to different window.

Here is a link to see what shops look likes and our intern shop visual : https://files.cloudmarel.example/u/58302917/RTB/Marketing/visual_elements.zip

Our Website : www.allortb.fr

• A broken phone
Big visual
Place for partner (Vorlex, Trelva, etc) logos, 4 or 8

```html
<!DOCTYPE html>
<html lang="fr">
<head>
<meta charset="utf-8">
<title>RTB, le SAV de votre mobile</title>
<link rel="stylesheet" href="https://fonts.googleapis.com/css2?family=Arimo:wght@400;700&family=Open+Sans:wght@400;600&display=swap">
<style>
  :root {
    --brand-red: #b01e2f;
    --brand-grey: #444245;
    --strip-grey: #e2dfdd;
    --text-dark: #333333;
    --partner-grey: #5b5b66;
    --white: #ffffff;
  }
  * { margin: 0; padding: 0; box-sizing: border-box; }
  html, body { width: 1200px; height: 1200px; overflow: hidden; background: var(--white); }
  .poster { position: relative; width: 1200px; height: 1200px; background: var(--white); font-family: "Open Sans", sans-serif; }

  .hero-photo {
    position: absolute; left: 0; top: 0; width: 1200px; height: 726px;
    background: radial-gradient(ellipse 45% 40% at 58% 38%, #2a2b30 0%, #3b3c42 55%, rgba(255,255,255,0) 100%),
                linear-gradient(180deg, #ffffff 0%, #f4f4f4 100%);
  }

  .headline-band {
    position: absolute; left: 0; top: 726px; width: 1197px; height: 190px;
    background: var(--brand-red);
  }
  .headline {
    position: absolute; left: 362px; top: 742px;
    font-family: "Arimo", sans-serif; font-weight: 400;
    font-size: 82px; line-height: 76px; color: var(--white); letter-spacing: -1px;
  }

  .exclaim { position: absolute; left: 960px; top: 590px; width: 120px; height: 310px; }

  .services-strip {
    position: absolute; left: 316px; top: 918px; width: 881px; height: 33px;
    background: var(--strip-grey);
    display: flex; align-items: center; justify-content: center;
    font-size: 14.5px; color: var(--text-dark); white-space: nowrap;
  }
  .services-strip .sep { margin: 0 8px; }

  .brand-mark {
    position: absolute; left: 33px; top: 763px; width: 279px; height: 278px;
    background: var(--brand-grey); border: 2px solid var(--white);
    display: flex; flex-direction: column; justify-content: flex-end;
    padding: 0 28px 40px 0; align-items: flex-end;
    font-family: "Arimo", sans-serif; font-weight: 400; color: var(--white);
    text-align: right;
  }
  .brand-mark .name { font-size: 40px; line-height: 42px; }

  .partners {
    position: absolute; left: 400px; top: 985px; width: 720px; height: 60px;
    display: flex; align-items: center; justify-content: space-around;
    font-family: "Arimo", sans-serif; font-weight: 700; font-size: 22px;
    color: var(--partner-grey);
  }

  .footer-line {
    position: absolute; left: 72px; top: 1128px;
    font-size: 15.5px; color: var(--text-dark); white-space: nowrap;
  }
  .footer-line .site { color: var(--brand-red); font-weight: 600; font-size: 18px; margin-left: 10px; }
</style>
</head>
<body>
<main class="poster">
  <div class="hero-photo" role="img" aria-label="Photo d'un smartphone noir à l'écran fissuré, ouvert par une main tenant une spatule métallique, sur fond blanc"></div>

  <div class="headline-band"></div>
  <h1 class="headline">RTB, le SAV<br>de votre mobile</h1>

  <svg class="exclaim" viewBox="0 0 120 310" aria-hidden="true">
    <polygon points="80,3 113,7 72,232 48,230" fill="var(--white)" stroke="var(--brand-red)" stroke-width="2"/>
    <polygon points="22,262 60,264 55,303 17,301" fill="var(--white)"/>
  </svg>

  <div class="services-strip">
    <span>Réparations</span><span class="sep">I</span>
    <span>Sauvegardes</span><span class="sep">I</span>
    <span>Mises à jour</span><span class="sep">I</span>
    <span>Prêts et location</span><span class="sep">I</span>
    <span>Diagnostics</span><span class="sep">I</span>
    <span>Rénovations</span><span class="sep">I</span>
    <span>Recyclage</span><span class="sep">I</span>
    <span>Accessoires</span>
  </div>

  <div class="brand-mark">
    <span class="name">relais<br>tech<br>boutiques</span>
  </div>

  <div class="partners">
    <span>Solvane</span>
    <span>Vorlex</span>
    <span>Kelmo</span>
    <span>Marvota</span>
    <span>Trelva</span>
  </div>

  <p class="footer-line">Retrouvez tout le détail de nos offres Relais Tech Boutiques &amp; Relais Tech Multimédia sur<span class="site">www.allortb.fr</span></p>
</main>
</body>
</html>
```